Wochen Speiseplan
Zielgruppe
Hospiz
Aufgabenstellung
Wir brauchen für unser Hospiz einen Wochenspeiseplan. Es soll eine Powerpointseite im A4 Format erstellt werden. Wir brauchen 4 unterschiedliche Seiten - für jede Jahreszeit einen Entwurf. Der Speiseplan soll von uns selbst ausgefüllt werden können.
Inhalte: Montag - Sonntag jeweils Mittag- und Abendessen. (Aufgebaut wie ein Stundenplan.). Möglichst große Schriftgröße. In der Fußnote bitte: "Änderungen vorbehalten schreiben". Das ganze soll professionell, aber dennoch liebevoll gestaltet sein. Es soll unseren Bewohnern "Liust machen" draufzuschauen. Der Plan wird jede Woche neu ausgefüllt, ausgedruckt und laminiert. Sollte also einfach zu handhaben sein.
Das Hospiz lebt von Spenden, daher bitte nicht zu aufwendig, dafür aber bezahlbar machen.

```html
<!DOCTYPE html>
<html lang="de">
<head>
<meta charset="utf-8">
<title>Speiseplan</title>
<link rel="stylesheet" href="https://fonts.googleapis.com/css2?family=Pinyon+Script&display=swap">
<style>
  :root {
    --plum: #8c7d9e;
    --plum-dark: #5e5071;
    --berry: #d9345f;
    --berry-light: #f3a2b9;
    --frost: #f7dbe4;
    --panel: rgba(255, 255, 255, 0.42);
    --ink: #111111;
    --title-fill: #fff1f3;
    --title-stroke: #d8324f;
    --greeting-fill: #f49a8c;
  }
  html, body {
    margin: 0;
    padding: 0;
    overflow: hidden;
    background: #ffffff;
  }
  .sheet {
    position: relative;
    width: 1200px;
    height: 848px;
    overflow: hidden;
    font-family: Arial, Helvetica, sans-serif;
    color: var(--ink);
  }
  .backdrop {
    position: absolute;
    inset: 0;
    background:
      radial-gradient(circle at 27% 27%, var(--berry-light) 0 9%, transparent 14%),
      radial-gradient(circle at 50% 26%, var(--berry) 0 12%, transparent 18%),
      radial-gradient(circle at 73% 24%, var(--berry) 0 9%, transparent 15%),
      radial-gradient(circle at 88% 32%, var(--berry-light) 0 10%, transparent 16%),
      radial-gradient(circle at 18% 62%, var(--berry-light) 0 12%, transparent 19%),
      radial-gradient(circle at 50% 70%, var(--frost) 0 13%, transparent 20%),
      radial-gradient(circle at 83% 68%, var(--berry-light) 0 12%, transparent 19%),
      linear-gradient(135deg, var(--plum) 0%, var(--plum-dark) 45%, var(--plum) 100%);
  }
  .script {
    position: absolute;
    font-family: "Pinyon Script", cursive;
    margin: 0;
    font-weight: 400;
    line-height: 1;
  }
  .greeting {
    color: var(--greeting-fill);
    -webkit-text-stroke: 1.5px #ffffff;
    font-size: 104px;
  }
  .greeting-top { left: 46px; top: 78px; }
  .greeting-bottom { left: 112px; top: 210px; }
  .title {
    left: 300px;
    top: 58px;
    font-size: 190px;
    color: var(--title-fill);
    -webkit-text-stroke: 2px var(--title-stroke);
  }
  .plan-panel {
    position: absolute;
    left: 80px;
    top: 339px;
    width: 1037px;
    height: 468px;
    background: var(--panel);
  }
  .grid-lines {
    position: absolute;
    left: 0;
    top: 0;
    width: 1200px;
    height: 848px;
  }
  .day, .meal {
    font-family: "Pinyon Script", cursive;
    position: absolute;
    font-size: 44px;
    line-height: 1;
  }
  .meal { font-size: 40px; line-height: 0.95; }
  .dish {
    position: absolute;
    top: 418px;
    font-size: 18px;
    line-height: 1.33;
  }
  .week {
    position: absolute;
    left: 80px;
    top: 808px;
    font-size: 27px;
  }
  .note {
    position: absolute;
    right: 4px;
    top: 824px;
    font-size: 17px;
  }
</style>
</head>
<body>
<main class="sheet">
  <div class="backdrop" role="img" aria-label="Foto von bereiften roten Beeren an einem Zweig vor violettem Hintergrund"></div>

  <p class="script greeting greeting-top">Guten</p>
  <p class="script greeting greeting-bottom">Appetit!</p>
  <h1 class="script title">Speiseplan</h1>

  <div class="plan-panel"></div>

  <svg class="grid-lines" viewBox="0 0 1200 848" aria-hidden="true">
    <g stroke="#000" stroke-width="4" stroke-dasharray="7 9" fill="none">
      <line x1="258" y1="360" x2="258" y2="786"/>
      <line x1="383" y1="360" x2="383" y2="786"/>
      <line x1="508" y1="360" x2="508" y2="786"/>
      <line x1="634" y1="360" x2="634" y2="786"/>
      <line x1="759" y1="360" x2="759" y2="786"/>
      <line x1="884" y1="360" x2="884" y2="786"/>
      <line x1="1010" y1="360" x2="1010" y2="786"/>
      <line x1="108" y1="573" x2="1085" y2="573"/>
    </g>
  </svg>

  <span class="day" style="left:272px;top:356px">Mo</span>
  <span class="day" style="left:398px;top:356px">Di</span>
  <span class="day" style="left:524px;top:356px">Mi</span>
  <span class="day" style="left:650px;top:356px">Do</span>
  <span class="day" style="left:776px;top:356px">Fr</span>
  <span class="day" style="left:912px;top:356px">Sa</span>
  <span class="day" style="left:1030px;top:356px">So</span>

  <span class="meal" style="left:96px;top:412px">Mittag-<br>&nbsp;&nbsp;Essen</span>
  <span class="meal" style="left:104px;top:650px">Abend-<br>&nbsp;Essen</span>

  <p class="dish" style="left:276px;margin:0">Spargel-<br>suppe<br>&amp; Dessert</p>
  <p class="dish" style="left:391px;margin:0">Schweine-<br>medallions<br>in Champig-<br>non-Sahne-<br>Soße mit<br>Kroketten</p>
  <p class="dish" style="left:524px;margin:0">Rindergu-<br>lasch mit<br>Nudeln<br>dazu Salat</p>
  <p class="dish" style="left:649px;margin:0">Schnitzel<br>Wiener Art<br>mit div.<br>Beilagen<br>dazu Salat</p>
  <p class="dish" style="left:780px;margin:0">Tomaten-<br>crem-<br>suppe<br>dazu<br>Ciabatta</p>

  <p class="week" style="margin:0">Woche vom 07.04.2014 bis 13.04.2014</p>
  <p class="note" style="margin:0">*Änderungen vorbehalten*</p>
</main>
</body>
</html>
```